Упаковка снеков из морской капусты
Задание на дизайн
Приоритеты объектов в упаковке
Знак производителя, Марка продукта, Вид продукта, Название продукта, Иллюстрация
Опишите свою организацию или продукт и целевую аудиторию
сушеная морская капуста спрессованная в тончайшие пропускающие свет листы,
она настолько высушена, что хрустит ломаясь и буквально тает во рту впитывая влагу. это очень вкусно, хочется есть еще и еще...во вторых это очень полезный продукт, это здоровье ,энергия, для тех кого любит удача и у которых большие планы кто знает что хочет от жизни.
Приложите логотипы или другие материалы
это обычная очень типичная упаковка
может сделать гоизонт общий преходящий на правую и левую стороны там с одной стороны красивая фигура мужчины с другой женщины
так выглядит сам продукт 10 тончайших пластинок спрессованной сушеной капусты
здесь красивый шрифт ,сам продукт и выдержана цветовая гамма
ИНФОРМАЦИОННЫЕ ЗНАЧКИ
Вот так выглядит сам продукт
здесь есть типа талисман
ЛОГОТИПЫ
Комментарии и пожелания для дизайнеров
хотелось бы увидеть оригинальные решения, обыграть саму упаковку (использовать боковые стороны),использовать например черно-белое фото и яркие цветные акценты...показать энергию, молодость, здоровье, успех...идея или две упаковки: для желающих вести здоровый образ мужчин и для довольных своей фигурой и счастливых женщин...или создать в одной упаковке и для мужчин и женщин. можно совсем немного добавить Азии например иероглиф ...возможны два вкуса васаби и оливок. Можно сделать две упаковки так, чтобы рисунок на одной был продолжением на другой и когда они стоят вместе на полке смотрятся как единое целое...может какие то другие идеи...

```html
<!DOCTYPE html>
<html lang="ru">
<head>
<meta charset="utf-8">
<title>Снеки из морской капусты — упаковка</title>
<link rel="stylesheet" href="https://fonts.googleapis.com/css2?family=Amatic+SC:wght@400;700&family=Ruslan+Display&family=Jura:wght@500&display=swap">
<style>
  :root {
    --bg: #f4f6f6;
    --pack: #1e6b1d;
    --pack-dark: #124a12;
    --pack-light: #2c8a2a;
    --teal: #34b4c6;
    --yellow: #f6c515;
    --orange: #f3a10f;
    --ink: #101410;
    --lime: #d8e64a;
    --pink: #e8306a;
    --white: #ffffff;
  }
  * { margin: 0; padding: 0; box-sizing: border-box; }
  html, body { width: 1200px; height: 800px; overflow: hidden; background: var(--bg); }
  .canvas { position: relative; width: 1200px; height: 800px; }

  .pack {
    position: absolute; left: 370px; top: 30px; width: 460px; height: 740px;
    background: linear-gradient(90deg, var(--pack-dark) 0%, var(--pack) 12%, var(--pack-light) 50%, var(--pack) 88%, var(--pack-dark) 100%);
    border-radius: 6px;
    box-shadow: 0 18px 40px rgba(0,0,0,.18);
    overflow: hidden;
  }
  .pack__seal {
    position: absolute; left: 0; right: 0; height: 46px;
    background: repeating-linear-gradient(180deg, rgba(0,0,0,.18) 0 2px, transparent 2px 6px);
  }
  .pack__seal--top { top: 0; border-top: 7px solid var(--teal); }
  .pack__seal--bottom { bottom: 0; }
  .pack__tab {
    position: absolute; right: 0; top: 120px; width: 16px; height: 70px; background: var(--teal);
  }

  .title {
    position: absolute; top: 112px; left: 0; right: 0; text-align: center;
    font-family: "Ruslan Display", serif; font-size: 88px; line-height: 1;
    color: var(--yellow);
    -webkit-text-stroke: 6px var(--ink); paint-order: stroke fill;
    letter-spacing: 2px;
  }
  .subtitle {
    position: absolute; top: 225px; left: 0; right: 0; text-align: center;
    font-family: "Amatic SC", sans-serif; font-weight: 700; font-size: 34px;
    color: var(--white); letter-spacing: 1px;
  }
  .flavour { position: absolute; top: 270px; left: 110px; width: 240px; height: 80px; }
  .flavour__label {
    position: absolute; left: 0; right: 0; text-align: center; line-height: 1;
    font-family: "Jura", sans-serif; font-weight: 500; letter-spacing: 3px;
  }
  .flavour__kind { top: 8px; font-size: 18px; color: var(--white); }
  .flavour__taste { top: 42px; font-size: 19px; color: var(--white); }

  .slogans {
    position: absolute; top: 370px; left: 0; right: 0; text-align: center;
    font-family: "Amatic SC", sans-serif; font-size: 44px; line-height: 1.35;
    color: var(--lime); letter-spacing: 1px; list-style: none;
  }
  .waves { position: absolute; left: 10px; top: 455px; }
  .chevrons { position: absolute; right: 18px; top: 480px; }

  .brand {
    position: absolute; bottom: 70px; left: 0; right: 0;
    display: flex; align-items: center; justify-content: center; gap: 12px;
    font-family: "Jura", sans-serif; font-weight: 500; font-size: 34px;
    color: var(--white); letter-spacing: 6px;
  }
  .brand__dot { width: 26px; height: 26px; border-radius: 50%; background: var(--teal); }
  .weight {
    position: absolute; bottom: 52px; left: 14px; padding: 1px 6px;
    background: var(--teal); color: var(--ink);
    font-family: "Jura", sans-serif; font-size: 13px;
  }
</style>
</head>
<body>
<main class="canvas">
  <section class="pack" aria-label="Упаковка снеков из морской капусты, вкус оливки">
    <div class="pack__seal pack__seal--top"></div>
    <div class="pack__tab"></div>

    <h1 class="title">Снеки</h1>
    <p class="subtitle">из морской капусты</p>

    <div class="flavour">
      <svg width="240" height="80" viewBox="0 0 240 80" aria-hidden="true">
        <g stroke="#ffffff" stroke-width="1.5" fill="none">
          <path d="M44 17 H84"/>
          <path d="M44 17 l6 -4 M44 17 l6 4"/>
          <path d="M156 17 H196"/>
          <path d="M196 17 l-6 -4 M196 17 l-6 4"/>
        </g>
        <path d="M8 42 L30 40 L24 52 L30 66 L8 62 Z" fill="#c97e06"/>
        <path d="M232 42 L210 40 L216 52 L210 66 L232 62 Z" fill="#c97e06"/>
        <path d="M24 38 Q120 28 216 38 L216 64 Q120 54 24 64 Z" fill="#f3a10f"/>
      </svg>
      <span class="flavour__label flavour__kind">вкус</span>
      <span class="flavour__label flavour__taste">оливки</span>
    </div>

    <ul class="slogans">
      <li>суперполезно</li>
      <li>ну очень вкусно</li>
      <li>хрум-хрум</li>
    </ul>

    <svg class="waves" width="80" height="80" viewBox="0 0 80 80" aria-hidden="true">
      <g fill="none" stroke="#e8306a" stroke-width="5" stroke-linecap="round">
        <path d="M4 14 q9 -10 18 0 t18 0 t18 0 t18 0"/>
        <path d="M4 40 q9 -10 18 0 t18 0 t18 0 t18 0"/>
        <path d="M4 66 q9 -10 18 0 t18 0 t18 0 t18 0"/>
      </g>
    </svg>

    <svg class="chevrons" width="56" height="52" viewBox="0 0 56 52" aria-hidden="true">
      <g fill="none" stroke="#f6c515" stroke-width="4">
        <path d="M2 4 L28 14 L54 4"/>
        <path d="M2 20 L28 30 L54 20"/>
        <path d="M2 36 L28 46 L54 36"/>
      </g>
    </svg>

    <div class="brand"><span class="brand__dot"></span><span class="brand__name">MARELIA</span></div>
    <span class="weight">25г</span>
    <div class="pack__seal pack__seal--bottom"></div>
  </section>
</main>
</body>
</html>
```